Maple Roadway Handbook
2nd Edition
Love #26 and #28 and #33
The graphics are original, they don't make it appear as if I am promoting Driving drunk and they have good graphic appeal.
I don't want to seem like I am promoting Driving drunk so #32 (and #19 and #29)seem to dance a little too close to the edge.
#25 -Awesome job! I need you to post a version with
1) No text on the back cover
2) No publisher's logo and location
3) No ISBN number or bar code
3) No photo (leave the white box under neath the photo)
4) No text on the spine
I like that this cover is implementing a graphic of some sort (the swirly thingy). I am not wild about brown though.
I would recommend getting rid of the glow around the subtext and the underline on the very top. However, I don't know that I would choose this design idea even if it was executed perfectly.
Take your designs in a whole new direction. The fonts and text locations are easy to tweak, the hard part is thinking of a unique graphic to make the focus of the cover. Most of the submissions so far have implement text and colored rectangles, so try to think of a stock photo or a graphic or a shape that will grab the attention, and then worry about the text later.
I am hoping for someone to submit designs that implement graphics, photos, or something more than a few two-toned rectangles.
#6 and #7 are nearly exact copies of the first edition only the color is changed slightly. I will not choose a submission that is essentially a version of the first edition.
#5 This is almost an exact replica of the first edition only its blue. I am not interested in designs that look similar to the first edition.
#3 The big gold start is not a wholly bad element, but I think having it front and center, makes it too prominent.
General Comment.
The Back cover of this book will have:
1) an ISBN
2)Text
3) A photo
4)the publishers logo
HOWEVER - The design we choose will not have any of those elements included. We will be altering the photo, text, ect. and pasting then on top of the design chosen here.
I think it is really helpful to include some place holder, text, photos, isbn ect. on your initial submissions so we can see how the elements will fit into your back cover layout, but once we have zeroed in on a design we like, we will need to have those elements removed.
#2 and #3 I am not wild about the colors.
#1 The title font is a bit cartoonist, which doesn't work well for a law firm trying to impress clientele. Also, all the text is crammed into the top of the cover, leaving a large blank space in the bottom 2/3.
I would reexamine your font selection. take a look at some professional text books and reference books. I would also consider how to balance the test at the top with the emptiness at the bottom. Once again, take a look at other professional text and reference books for ideas.
#4 I like the the colors and the different color blocks, but I am not wild about the word "Handbook" written vertically. I feel like something should be written there, but I am not sure about what, and the word "handbook" is not something that is particularly important or deserves emphasis.
Submissions #4,3,& 2 I appreciate you doing a mock up of the back page, but the your final submission should not have the text, picture, publisher's logo, or the ISBN. All of those items will be pasted ontop of your submission after the fact. You can go ahead an add them just so I can see what it would look like, but final submission would need to be altered.

```html
<!DOCTYPE html>
<html lang="en">
<head>
<meta charset="utf-8">
<title>The Maple Roadway Handbook – Cover Spread</title>
<link href="https://fonts.googleapis.com/css2?family=Open+Sans:wght@400;600;700&display=swap" rel="stylesheet">
<style>
  :root {
    --page: #ffffff;
    --cover-black: #0b0b0b;
    --strip-black: #161616;
    --band-grey: #5a5a5a;
    --accent-orange: #f04a12;
    --accent-red: #c8200a;
    --tagline-yellow: #f7c21a;
    --placeholder-line: #2a2a2a;
    --text-white: #ffffff;
    --photo-sky: #8fa6b2;
    --photo-ground: #4e5a3c;
  }
  * { margin: 0; padding: 0; box-sizing: border-box; }
  html, body { width: 1200px; height: 816px; overflow: hidden; background: var(--page); }
  body { position: relative; font-family: "Open Sans", Arial, sans-serif; color: var(--text-white); }

  .cover { position: absolute; top: 53px; height: 701px; background: var(--cover-black); overflow: hidden; }

  /* Back cover */
  .back-cover { left: 86px; width: 464px; }
  .back-cover .top-strip { position: absolute; left: 0; top: 0; width: 100%; height: 22px; background: var(--strip-black); }
  .placeholder-label { position: absolute; font-size: 17px; font-weight: 400; line-height: 24px; }
  .label-text1 { left: 34px; top: 28px; font-weight: 700; }
  .label-text2 { left: 305px; top: 71px; }
  .label-text3 { left: 28px; top: 302px; }
  .label-logo { left: 86px; top: 518px; }
  .label-isbn { left: 365px; top: 518px; }
  .photo-slot {
    position: absolute; left: 22px; top: 72px; width: 156px; height: 142px;
    border: 1px solid var(--placeholder-line);
  }
  .photo-slot span { position: absolute; left: 0; right: 0; top: 22px; text-align: center; font-size: 17px; font-weight: 700; line-height: 24px; }
  .back-cover .rule-grey { position: absolute; left: 0; top: 606px; width: 100%; height: 4px; background: var(--band-grey); }
  .back-cover .band-orange { position: absolute; left: 0; top: 611px; width: 100%; height: 20px; background: linear-gradient(var(--accent-orange), var(--accent-red)); }

  /* Front cover */
  .front-cover { left: 636px; width: 473px; }
  .swirl-art {
    position: absolute; left: 0; top: 0; width: 100%; height: 56px;
    background: linear-gradient(170deg, var(--cover-black) 0%, #3a140a 45%, #8a2a0c 75%, var(--cover-black) 100%);
  }
  .title-panel {
    position: absolute; left: 0; top: 56px; width: 100%; height: 106px;
    background: linear-gradient(90deg, rgba(70,70,70,0.55), rgba(90,90,90,0.75));
  }
  .book-title {
    position: absolute; left: 0; top: 62px; width: 100%;
    text-align: center; font-size: 31px; font-weight: 600; line-height: 41px;
  }
  .edition { position: absolute; right: 58px; top: 265px; font-size: 19px; font-weight: 400; line-height: 26px; }
  .front-cover .rule-grey { position: absolute; left: 0; top: 298px; width: 100%; height: 6px; background: var(--band-grey); }
  .front-cover .band-orange { position: absolute; left: 0; top: 304px; width: 100%; height: 12px; background: linear-gradient(var(--accent-orange), var(--accent-red)); }
  .cover-photo {
    position: absolute; left: 0; top: 316px; width: 100%; height: 272px;
    background: linear-gradient(180deg, var(--photo-sky) 0%, #6f8170 45%, var(--photo-ground) 100%);
  }
  .tagline {
    position: absolute; left: 12px; top: 484px; width: 385px;
    color: var(--tagline-yellow); font-size: 18px; font-weight: 600; line-height: 27px;
    text-shadow: 1px 1px 2px #000, -1px -1px 2px #000;
  }
  .author { position: absolute; left: 0; top: 604px; width: 100%; text-align: center; font-size: 19px; font-weight: 600; line-height: 28px; }
</style>
</head>
<body>

<section class="cover back-cover" aria-label="Back cover">
  <div class="top-strip"></div>
  <div class="placeholder-label label-text1">Text 1</div>
  <div class="photo-slot"><span>Photo</span></div>
  <div class="placeholder-label label-text2">Text 2</div>
  <div class="placeholder-label label-text3">Text 3</div>
  <div class="placeholder-label label-logo">Logo</div>
  <div class="placeholder-label label-isbn">ISBN</div>
  <div class="rule-grey"></div>
  <div class="band-orange"></div>
</section>

<section class="cover front-cover" aria-label="Front cover">
  <div class="swirl-art" role="img" aria-label="Decorative sweeping orange and red swirl graphic across the top of the cover"></div>
  <div class="title-panel"></div>
  <h1 class="book-title">The Maple Roadway<br>Handbook</h1>
  <div class="edition">Second Edition</div>
  <div class="rule-grey"></div>
  <div class="band-orange"></div>
  <div class="cover-photo" role="img" aria-label="Photo of a police officer speaking with a driver seated in a car on a suburban street"></div>
  <p class="tagline">Answers to 40 Common Questions and Everything Else You Need to Know About DUIs</p>
  <div class="author">Thomas R. Barwick, Esq.</div>
</section>

</body>
</html>
```